American Ingenuity + Italian Design = RTB
International consulting services from fine arts/advertising/construction & special events. A new company that will find the right connections to get your job done.

Card should include -
1. Company Name with logo: rosalind tavore Enterprises LLC
2. Address: 218 Dunmore Lane, Highland Springs, VA 23081
3. Phone Number: 804.512.3096 (US)
4. Tagline: American Ingenuity + Italian Style + RTB (you can improve on this idea)
5. web address to be added eventually

Likes: airplanes and boats to give the idea of movement & international ability
Logo: if you have an idea to adjust the colors, we are open to that. Rosalind likes blues, but other colors didn't seem to work; remember this will print 4c in most cases)
Updates

I have uploaded the logo on it's own. Typical business card size for the US is 3.5" x 2", but doesn't have to be that size. the flyer was just for reference of something else that was done and to give some background. I hope that didn't confuse anyone.

Thank you all for the amazing work in the tight deadline. We will be reviewing everything today and will provide feedback by tomorrow. I will also pass this site on to anyone I know looking for design work.

website address rosalindtavore.example email rosalind@rosalindtavore.example Italian number +39 347 861 2054 USA 1 804 512 3096 International Consulting Services American Ingenuity. Italian Design. rtB These are the vital elements for the card. In addition please note the new fotos should have been uploaded. Best Regards

Target Market(s)

Companies or individuals that want to bring the Italian flair to the US or American know how to Italian projects. This can range from a bride planning a destination wedding, an interior designer looking to add pieces or knowledge to their project, or an investor looking to buy property to invest and build.

Industry/Entity Type

Construction

Requirements
Must have
• 1. Company Name with logo: rosalind tavore Enterprises LLC
+39 347 861 2054 (Italia)
Nice to have
• incorporate the idea of international ability; airplanes (like the wing in the background of the logo)
Should not have
• not overly decorative

```html
<!DOCTYPE html>
<html lang="en">
<head>
<meta charset="utf-8">
<title>Rosalind Tavore Enterprises LLC — Business Card</title>
<link rel="stylesheet" href="https://fonts.googleapis.com/css2?family=Open+Sans:wght@400;600&display=swap">
<style>
  :root {
    --stage: #1b1918;
    --card-dark: #2f3236;
    --card-dark-2: #3a3e43;
    --sky-top: #2a2f36;
    --sky-mid: #4a5058;
    --sky-low: #6a6e72;
    --ink-light: #eef0f2;
    --ink-muted: #c9ccd0;
    --brand-blue: #2b8fd6;
    --band-white: #ffffff;
    --rule: #8a8f95;
  }
  * { box-sizing: border-box; margin: 0; padding: 0; }
  html, body { width: 1200px; height: 716px; overflow: hidden; background: var(--stage); }
  body { font-family: "Open Sans", Arial, sans-serif; position: relative; }

  .card {
    position: absolute;
    top: 215px;
    width: 500px;
    height: 286px;
    overflow: hidden;
    box-shadow: 0 6px 18px rgba(0,0,0,.5);
  }

  /* Front */
  .card-front { left: 70px; background: var(--card-dark); }
  .card-front .photo-fill {
    position: absolute; inset: 0;
    background: linear-gradient(160deg, var(--sky-top) 0%, var(--sky-mid) 48%, var(--sky-low) 62%, var(--sky-top) 100%);
    opacity: .85;
  }
  .card-front .service-line {
    position: absolute; top: 28px; left: 0; right: 0;
    text-align: center; color: var(--ink-light);
    font-size: 17px; letter-spacing: .2px;
  }
  .card-front .brand-name {
    position: absolute; top: 108px; left: 0; right: 0;
    text-align: center; color: var(--ink-light);
    font-size: 46px; font-weight: 400; letter-spacing: 4px;
  }
  .card-front .tagline {
    position: absolute; bottom: 30px; left: 0; right: 0;
    text-align: center; color: var(--ink-light);
    font-size: 17px;
  }
  .card-front .tagline .mark { color: var(--brand-blue); }

  /* Back */
  .card-back { left: 630px; background: var(--card-dark); }
  .card-back .name-band {
    position: absolute; top: 0; left: 0; right: 0; height: 88px;
    background: var(--band-white);
    padding: 18px 24px 0 24px;
  }
  .name-band .company {
    color: var(--brand-blue); font-size: 27px; font-weight: 400; line-height: 1.1;
  }
  .name-band .web {
    color: #333; font-size: 13px; letter-spacing: 2px; margin-top: 6px; padding-left: 70px;
  }
  .card-back .texture {
    position: absolute; top: 88px; left: 0; right: 0; bottom: 0;
    background: linear-gradient(180deg, var(--card-dark-2), var(--card-dark));
  }
  .card-back .logo-panel {
    position: absolute; top: 104px; left: 18px; width: 196px; height: 160px;
    background: linear-gradient(170deg, #3d4247, #2c2f33);
    display: flex; align-items: center; justify-content: center;
    color: var(--brand-blue); font-size: 40px; letter-spacing: 4px;
  }
  .card-back .person {
    position: absolute; top: 104px; left: 236px; right: 20px;
  }
  .person .full-name {
    color: var(--brand-blue); font-size: 17px; font-weight: 600; letter-spacing: 1.5px;
  }
  .person .role { color: var(--ink-light); font-size: 12px; letter-spacing: 1px; margin-top: 2px; }
  .person .divider { height: 1px; background: var(--rule); margin: 10px 0 10px; width: 210px; }
  .contact-list { list-style: none; color: var(--ink-light); font-size: 12.5px; letter-spacing: .6px; line-height: 1.45; }
  .contact-list li { display: flex; align-items: flex-start; gap: 7px; }
  .contact-list svg { flex: none; margin-top: 4px; }
  .contact-list .address { display: block; }
</style>
</head>
<body>

  <section class="card card-front" aria-label="Card front">
    <div class="photo-fill" role="img" aria-label="Photo of an airplane wing over clouds and sea"></div>
    <p class="service-line">International Consulting Services</p>
    <p class="brand-name">RTB</p>
    <p class="tagline">American Ingenuity . Italian Design . <span class="mark">rtB</span></p>
  </section>

  <section class="card card-back" aria-label="Card back">
    <div class="name-band">
      <p class="company">rosalind tavore Enterprises LLC</p>
      <p class="web">www.rosalindtavore.example</p>
    </div>
    <div class="texture"></div>
    <div class="logo-panel" role="img" aria-label="Company name on dark photo panel">RTB</div>
    <div class="person">
      <p class="full-name">ROSALIND TAVORE</p>
      <p class="role">CEO</p>
      <div class="divider"></div>
      <ul class="contact-list">
        <li>
          <svg width="9" height="9" viewBox="0 0 10 10"><rect width="10" height="10" rx="1.5" fill="#eef0f2"/><path d="M3 2.5l1.2 1.5-.6.8a5 5 0 0 0 1.6 1.6l.8-.6L7.5 7 6.8 8C4.5 7.6 2.4 5.5 2 3.2z" fill="#2f3236"/></svg>
          <span>804.512.3096 (USA)</span>
        </li>
        <li>
          <svg width="9" height="9" viewBox="0 0 10 10"><rect width="10" height="10" rx="1.5" fill="#eef0f2"/><path d="M3 2.5l1.2 1.5-.6.8a5 5 0 0 0 1.6 1.6l.8-.6L7.5 7 6.8 8C4.5 7.6 2.4 5.5 2 3.2z" fill="#2f3236"/></svg>
          <span>+39 347 861 2054 (Italian)</span>
        </li>
        <li>
          <svg width="9" height="9" viewBox="0 0 10 10"><rect width="10" height="10" rx="1.5" fill="#eef0f2"/><path d="M2 3h6v4H2z M2 3l3 2.2L8 3" fill="none" stroke="#2f3236" stroke-width=".9"/></svg>
          <span>rosalind@rosalindtavore.example</span>
        </li>
        <li>
          <svg width="9" height="9" viewBox="0 0 10 10"><rect width="10" height="10" rx="1.5" fill="#eef0f2"/><path d="M5 8.5S2.6 5.8 2.6 4.2a2.4 2.4 0 0 1 4.8 0C7.4 5.8 5 8.5 5 8.5z" fill="#2f3236"/></svg>
          <span class="address">218 Dunmore Lane<br>Highland Springs, VA<br>23081</span>
        </li>
      </ul>
    </div>
  </section>

</body>
</html>
```